Creative Brief
tarnell financial llc .com
tarnellfinancial.example
I need double sided standard sized Business Card [3.5" x 2"]
just keep logo in mind
Professional
Dale Tarnell
President
4178 E. K Ave.
Greeley, CO 80219
dale@tarnellfinancial.example
I was in a logo contest, please utilize that design
as you see fit

```html
<!DOCTYPE html>
<html lang="en">
<head>
<meta charset="UTF-8">
<title>Tarnell Financial – Business Card</title>
<link href="https://fonts.googleapis.com/css2?family=Arimo:wght@400;700&display=swap" rel="stylesheet">
<style>
  :root {
    --page-bg: #e9e9e6;
    --card-bg: #ffffff;
    --brand-blue: #1d5ea8;
    --brand-green: #3f9a34;
    --text-dark: #2b2b2b;
    --icon: #444444;
  }
  * { box-sizing: border-box; margin: 0; padding: 0; }
  html, body {
    width: 1200px; height: 778px; overflow: hidden;
    background: var(--page-bg);
    font-family: "Arimo", Arial, sans-serif;
  }
  .card {
    position: absolute; left: 75px; top: 89px;
    width: 1050px; height: 600px;
    background: var(--card-bg);
    box-shadow: 0 4px 18px rgba(0,0,0,0.18);
    overflow: hidden;
  }
  .brand-mark {
    position: absolute; left: 225px; top: 60px;
    width: 110px; height: 110px;
    background: var(--brand-blue);
  }
  .brand-name {
    position: absolute; left: 64px; top: 216px;
    font-size: 27px; font-weight: 700;
    color: var(--brand-blue); letter-spacing: 0.3px;
    white-space: nowrap;
  }
  .holder {
    position: absolute; right: 70px; top: 70px; text-align: right;
  }
  .holder-name { font-size: 32px; font-weight: 700; color: var(--brand-blue); line-height: 1.1; }
  .holder-title { font-size: 24px; font-weight: 700; color: var(--brand-green); margin-top: 8px; }
  .address {
    position: absolute; left: 56px; top: 326px;
    font-size: 24px; line-height: 38px; color: var(--text-dark);
    font-style: normal;
  }
  .contacts {
    position: absolute; left: 56px; top: 422px; list-style: none;
    font-size: 24px; color: var(--text-dark);
  }
  .contacts li { display: flex; align-items: center; height: 36px; }
  .contacts svg { width: 18px; height: 18px; margin-right: 12px; fill: var(--icon); }
  .accent-line {
    position: absolute; left: 0; bottom: 50px;
    width: 100%; height: 6px; background: var(--brand-green);
  }
  .base-band {
    position: absolute; left: 0; bottom: 0;
    width: 100%; height: 40px; background: var(--brand-blue);
  }
</style>
</head>
<body>
  <div class="card">
    <div class="brand-mark" aria-hidden="true"></div>
    <div class="brand-name">TARNELL FINANCIAL LLC .COM</div>

    <div class="holder">
      <div class="holder-name">Dale Tarnell</div>
      <div class="holder-title">President</div>
    </div>

    <address class="address">
      4178 E. K Ave.<br>
      Greeley, CO 80219
    </address>

    <ul class="contacts">
      <li><svg viewBox="0 0 24 24"><path d="M6.6 10.8a15.1 15.1 0 0 0 6.6 6.6l2.2-2.2a1 1 0 0 1 1-.25 11.4 11.4 0 0 0 3.6.57 1 1 0 0 1 1 1V20a1 1 0 0 1-1 1A17 17 0 0 1 3 4a1 1 0 0 1 1-1h3.5a1 1 0 0 1 1 1c0 1.25.2 2.45.57 3.57a1 1 0 0 1-.25 1z"/></svg>970-555-0142</li>
      <li><svg viewBox="0 0 24 24"><path d="M2 5h20v14H2z M4 7v.5l8 5 8-5V7z" fill-rule="evenodd"/></svg>dale@tarnellfinancial.example</li>
      <li><svg viewBox="0 0 24 24"><circle cx="12" cy="12" r="10"/></svg>www.tarnellfinancial.example</li>
    </ul>

    <div class="accent-line" aria-hidden="true"></div>
    <div class="base-band" aria-hidden="true"></div>
  </div>
</body>
</html>
```